Looking for a clean, modern, and professional business card design that reflects Valtrim Systems

The design should include the company logo, contact details, and align with our brand identity. Please use a sophisticated and minimalist style, incorporating [specific colors, if applicable]. Creativity is welcome, but the card must maintain a polished and professional appearance.

Details to Include:

Name: Gavin Trelowe
Title: VP Sales / Operations
Company: Valtrim Systems
Phone: 483.216.7705
Email: gavin@valtrimsystems-example.com
Website: www.valtrimsystems-example.com

```html
<!DOCTYPE html>
<html lang="en">
<head>
<meta charset="utf-8">
<title>Valtrim Systems – Business Card</title>
<link href="https://fonts.googleapis.com/css2?family=Montserrat:wght@400;500;700&display=swap" rel="stylesheet">
<style>
  :root {
    --bg: #cdd2d3;
    --card: #f1f1ef;
    --edge: #1f5aa8;
    --brand-blue: #3b7cc2;
    --ink: #141414;
    --text: #3a3a3a;
  }
  * { box-sizing: border-box; margin: 0; padding: 0; }
  html, body { width: 1200px; height: 881px; overflow: hidden; }
  body {
    background: var(--bg);
    font-family: "Montserrat", sans-serif;
    position: relative;
  }
  .card {
    position: absolute;
    left: 290px;
    width: 620px;
    height: 354px;
    background: var(--card);
    border-bottom: 4px solid var(--edge);
    box-shadow: 0 14px 30px rgba(0,0,0,0.18);
  }
  .card--front { top: 52px; }
  .card--back { top: 474px; }

  /* Front side */
  .front__brand {
    position: absolute;
    left: 34px;
    top: 150px;
    display: flex;
    align-items: center;
    gap: 10px;
  }
  .brand-mark {
    width: 14px; height: 14px;
    background: var(--brand-blue);
  }
  .brand-name {
    font-weight: 700;
    color: var(--ink);
    letter-spacing: 0.02em;
  }
  .front__brand .brand-name { font-size: 24px; }

  .front__divider {
    position: absolute;
    left: 300px;
    top: 60px;
    width: 2px;
    height: 234px;
    background: var(--brand-blue);
  }
  .contact {
    position: absolute;
    left: 322px;
    top: 62px;
    width: 285px;
    color: var(--text);
    font-size: 12.5px;
    line-height: 1.45;
  }
  .contact__name {
    font-size: 20px;
    font-weight: 700;
    color: var(--brand-blue);
    line-height: 1.2;
  }
  .contact__title { font-size: 13px; margin-bottom: 12px; }
  .contact__address { margin-bottom: 10px; }
  .contact__line {
    display: flex;
    align-items: center;
    gap: 8px;
    white-space: nowrap;
  }
  .contact__line svg { width: 12px; height: 12px; flex: none; fill: var(--brand-blue); }

  /* Back side */
  .back__brand {
    position: absolute;
    inset: 0;
    display: flex;
    align-items: center;
    justify-content: center;
    gap: 16px;
  }
  .back__brand .brand-mark { width: 26px; height: 26px; }
  .back__brand .brand-name { font-size: 46px; }
</style>
</head>
<body>

<section class="card card--front" aria-label="Business card front">
  <div class="front__brand">
    <span class="brand-mark"></span>
    <span class="brand-name">Valtrim Systems</span>
  </div>

  <div class="front__divider"></div>

  <div class="contact">
    <p class="contact__name">Gavin Trelowe</p>
    <p class="contact__title">VP Sales / Operations</p>
    <p class="contact__address">Valtrim Systems<br>27 Marlow Ct, SE Fairhaven,<br>VA 20199 United States</p>
    <p class="contact__line">
      <svg viewBox="0 0 24 24" aria-hidden="true"><path d="M6.6 10.8a15.1 15.1 0 0 0 6.6 6.6l2.2-2.2a1 1 0 0 1 1-.25 11.4 11.4 0 0 0 3.6.57 1 1 0 0 1 1 1V20a1 1 0 0 1-1 1A17 17 0 0 1 3 4a1 1 0 0 1 1-1h3.5a1 1 0 0 1 1 1c0 1.25.2 2.45.57 3.6a1 1 0 0 1-.25 1z"/></svg>
      483.216.7705
    </p>
    <p class="contact__line">
      <svg viewBox="0 0 24 24" aria-hidden="true"><path d="M2 5h20v14H2zm2 2v.5l8 5 8-5V7zm0 2.8V17h16V9.8l-8 5z"/></svg>
      gavin@valtrimsystems-example.com
    </p>
    <p class="contact__line">
      <svg viewBox="0 0 24 24" aria-hidden="true"><path d="M12 2a10 10 0 1 0 0 20 10 10 0 0 0 0-20zm6.9 9h-3a15 15 0 0 0-1.3-5.6A8 8 0 0 1 18.9 11zM12 4.1c.9 1.2 1.8 3.6 1.9 6.9h-3.8c.1-3.3 1-5.7 1.9-6.9zM4.1 13h3a15 15 0 0 0 1.3 5.6A8 8 0 0 1 4.1 13zm3-2h-3a8 8 0 0 1 4.3-5.6A15 15 0 0 0 7.1 11zm4.9 8.9c-.9-1.2-1.8-3.6-1.9-6.9h3.8c-.1 3.3-1 5.7-1.9 6.9zm2.6-1.3a15 15 0 0 0 1.3-5.6h3a8 8 0 0 1-4.3 5.6z"/></svg>
      www.valtrimsystems-example.com
    </p>
  </div>
</section>

<section class="card card--back" aria-label="Business card back">
  <div class="back__brand">
    <span class="brand-mark"></span>
    <span class="brand-name">Valtrim Systems</span>
  </div>
</section>

</body>
</html>
```